Biz Card for Harrowfield Property Partners - HWPP

Harrowfield Property Partners is a commercial real estate acquisitions firm. We buy commercial property and need to raise capital from investors for each deal we buy. The vibe needs to be: give us your money, we will multiply it.
Our website: www.hrwpp-example.com
Competitors are: https://velmarholdings-example.com/, https://tribanquepartners-example.com/, http://www.ostrellecapital-example.com/
Target Market(s)
High Net Worth Individuals, Bankers, Insurance Companies, Commercial Real Estate Brokers.
Industry/Entity Type
Investment Banking
Contact Information for Business Card
Name, Title, Addess, Cell#, Office#, email, website
Requirements
Must have
- use one of our logos. See website for look and feel: www.hrwpp-example.com
Nice to have
- see website: www.hrwpp-example.com

```html
<!DOCTYPE html>
<html lang="en">
<head>
<meta charset="utf-8">
<title>Harrowfield Property Partners — Business Card</title>
<link rel="stylesheet" href="https://fonts.googleapis.com/css2?family=Roboto:wght@300;400;500&display=swap">
<style>
  :root {
    --backdrop: #1e1e1e;
    --card: #ececec;
    --card-shade: #e2e2e2;
    --navy: #0f2540;
    --ink: #1c2a3a;
    --muted: #4a4f57;
    --strip: #55585c;
    --band-text: #e6e9ee;
  }
  * { margin: 0; padding: 0; box-sizing: border-box; }
  html, body { width: 1200px; height: 1138px; overflow: hidden; }
  body {
    background: var(--backdrop);
    font-family: "Roboto", sans-serif;
    position: relative;
  }
  .card {
    position: absolute;
    background: linear-gradient(180deg, var(--card) 0%, var(--card-shade) 100%);
    border-radius: 14px;
    overflow: hidden;
  }
  .card--front { left: 274px; top: 186px; width: 623px; height: 376px; }
  .card--back  { left: 276px; top: 608px; width: 618px; height: 374px; }

  .brand-dot { position: absolute; border-radius: 50%; background: var(--navy); }
  .brand-name {
    position: absolute;
    color: var(--navy);
    font-weight: 400;
    text-transform: uppercase;
    line-height: 1;
    white-space: nowrap;
  }
  .card--front .brand-dot { left: 85px; top: 111px; width: 128px; height: 128px; }
  .card--front .brand-name--main { left: 236px; top: 143px; font-size: 40px; letter-spacing: 3px; }
  .card--front .brand-name--sub  { left: 237px; top: 198px; font-size: 15px; letter-spacing: 5.6px; }
  .front-url {
    position: absolute; left: 0; right: 0; top: 332px;
    text-align: center; font-size: 15px; letter-spacing: 4px;
    color: var(--muted); font-weight: 300;
  }

  .person { position: absolute; left: 32px; top: 62px; }
  .person__name { font-size: 24px; color: var(--ink); font-weight: 400; }
  .person__title { font-size: 16px; color: var(--muted); font-weight: 300; margin-top: 4px; }

  .contact { position: absolute; left: 32px; top: 256px; list-style: none; }
  .contact li {
    display: flex; align-items: center; gap: 12px;
    font-size: 17px; color: var(--ink); font-weight: 300;
    height: 25px;
  }
  .contact svg { width: 14px; height: 14px; fill: var(--ink); }

  .card--back .brand-dot { left: 415px; top: 28px; width: 124px; height: 124px; }
  .card--back .brand-name--main { right: 30px; top: 165px; font-size: 30px; letter-spacing: 2.2px; }
  .card--back .brand-name--sub  { right: 31px; top: 206px; font-size: 12px; letter-spacing: 3.7px; }

  .address {
    position: absolute; right: 30px; top: 264px;
    text-align: right; font-size: 17px; line-height: 25px;
    color: var(--ink); font-weight: 300;
  }
  .bottom-strip {
    position: absolute; left: 0; bottom: 0; width: 320px; height: 16px;
    background: var(--strip);
  }
  .tagline-band {
    position: absolute; right: 0; bottom: 0; width: 322px; height: 46px;
    background: var(--navy);
    clip-path: polygon(22px 0, 100% 0, 100% 100%, 0 100%);
    display: flex; align-items: center; justify-content: flex-end;
    padding-right: 30px;
    color: var(--band-text); font-size: 17px; font-weight: 300;
  }
</style>
</head>
<body>
  <section class="card card--front">
    <div class="brand-dot"></div>
    <div class="brand-name brand-name--main">Harrowfield</div>
    <div class="brand-name brand-name--sub">Property Partners</div>
    <div class="front-url">www.hrwpp-example.com</div>
  </section>

  <section class="card card--back">
    <div class="person">
      <div class="person__name">Daniel R. Marsh</div>
      <div class="person__title">Managing Director</div>
    </div>

    <ul class="contact">
      <li>
        <svg viewBox="0 0 16 16"><path d="M3 2h3l1.5 3.5-2 1.2a8 8 0 0 0 3.8 3.8l1.2-2L14 10v3a1.5 1.5 0 0 1-1.5 1.5A11.5 11.5 0 0 1 1.5 3.5 1.5 1.5 0 0 1 3 2z"/></svg>
        (555) 014-2290
      </li>
      <li>
        <svg viewBox="0 0 16 16"><path d="M1 3h14v10H1zM2.5 4.5v.3L8 9l5.5-4.2v-.3zM2.5 6.6v5h11v-5L8 10.8z"/></svg>
        daniel@hrwpp-example.com
      </li>
      <li>
        <svg viewBox="0 0 16 16"><path d="M8 1a7 7 0 1 0 0 14A7 7 0 0 0 8 1zm0 1.3c.9 0 1.9 1.8 2.2 4.2H5.8C6.1 4.1 7.1 2.3 8 2.3zM2.4 7.4h2.5v1.2H2.4zm0 0M5.7 7.4h4.6v1.2H5.7zM11.1 7.4h2.5v1.2h-2.5zM5.8 9.5h4.4c-.3 2.4-1.3 4.2-2.2 4.2s-1.9-1.8-2.2-4.2z"/></svg>
        www.hrwpp-example.com
      </li>
    </ul>

    <div class="brand-dot"></div>
    <div class="brand-name brand-name--main">Harrowfield</div>
    <div class="brand-name brand-name--sub">Property Partners</div>

    <address class="address" style="font-style:normal">
      480 Linden Ave, Suite 900<br>
      Fairhaven, FL 33000
    </address>

    <div class="bottom-strip"></div>
    <div class="tagline-band">Commercial Real Estate Firm</div>
  </section>
</body>
</html>
```